Business cards for Remote DBA team

Business cards for team offering database administration, consultation, machine learning and AI services. As of now team is using both
www.fenrowlabs.cz and www.quillbarkgroup.cz URLs

Target Market(s)

IT managers

Industry/Entity Type

It Professional

Contact Information for Business Card

Should include logo
name, email, phone, twitter tag

Font styles to use
Sans Serif

Colors

Designer to choose colors to be used in the design.

```html
<!DOCTYPE html>
<html lang="en">
<head>
<meta charset="utf-8">
<title>Fenrow Labs – Business Card</title>
<link rel="stylesheet" href="https://fonts.googleapis.com/css2?family=Raleway:wght@300;400;700;800&family=Lato:wght@400&display=swap">
<style>
  :root {
    --backdrop: #141414;
    --card: #ffffff;
    --ink: #3d3d3f;
    --ink-soft: #5a5a5c;
    --brand: #1a8fd1;
    --brand-deep: #0b5fae;
    --brand-light: #4fb6ea;
    --icon-frame: #d9dde1;
  }
  * { margin: 0; padding: 0; box-sizing: border-box; }
  html, body {
    width: 1200px;
    height: 737px;
    overflow: hidden;
    background: var(--backdrop);
  }
  .card {
    position: absolute;
    left: 29px;
    top: 22px;
    width: 1143px;
    height: 683px;
    background: var(--card);
    overflow: hidden;
  }
  .card__art {
    position: absolute;
    inset: 0;
    width: 100%;
    height: 100%;
  }
  .brand {
    position: absolute;
    left: 97px;
    top: 88px;
    display: flex;
    align-items: center;
    gap: 16px;
  }
  .brand__dot {
    width: 46px;
    height: 46px;
    border-radius: 50%;
    background: var(--brand);
  }
  .brand__name {
    font-family: "Raleway", sans-serif;
    font-weight: 800;
    font-size: 32px;
    line-height: 1;
    letter-spacing: 0.5px;
    color: var(--brand);
    text-transform: uppercase;
  }
  .person {
    position: absolute;
    left: 91px;
    top: 226px;
  }
  .person__name {
    font-family: "Raleway", sans-serif;
    font-size: 44px;
    line-height: 1;
    color: var(--ink);
    text-transform: uppercase;
    letter-spacing: 0.3px;
  }
  .person__first { font-weight: 700; }
  .person__last { font-weight: 300; }
  .person__role {
    margin-top: 10px;
    font-family: "Raleway", sans-serif;
    font-weight: 400;
    font-size: 26px;
    color: var(--ink-soft);
  }
  .contacts {
    position: absolute;
    left: 96px;
    top: 386px;
    list-style: none;
  }
  .contact {
    display: flex;
    align-items: center;
    gap: 30px;
    margin-bottom: 30px;
  }
  .contact__icon {
    width: 50px;
    height: 50px;
    border: 2px solid var(--icon-frame);
    display: flex;
    align-items: center;
    justify-content: center;
    flex-shrink: 0;
  }
  .contact__icon svg { width: 30px; height: 30px; }
  .contact__text {
    font-family: "Lato", sans-serif;
    font-size: 27px;
    line-height: 36px;
    color: var(--ink);
  }
</style>
</head>
<body>
  <main class="card">
    <svg class="card__art" viewBox="0 0 1143 683" preserveAspectRatio="none" role="img" aria-label="Abstract blue technology pattern with circuit rings and connected nodes">
      <defs>
        <linearGradient id="techGradient" x1="0" y1="0" x2="1" y2="1">
          <stop offset="0" stop-color="#38a9e4"/>
          <stop offset="0.55" stop-color="#1a8fd1"/>
          <stop offset="1" stop-color="#0b5fae"/>
        </linearGradient>
        <linearGradient id="swooshGradient" x1="0" y1="1" x2="1" y2="0">
          <stop offset="0" stop-color="#0a4f96"/>
          <stop offset="1" stop-color="#4fb6ea"/>
        </linearGradient>
      </defs>
      <path d="M703 0 C 835 110, 870 420, 487 683 L1143 683 L1143 0 Z" fill="url(#techGradient)"/>
      <path d="M487 683 C 720 610, 960 470, 1143 360 L1143 683 Z" fill="url(#swooshGradient)" opacity="0.55"/>
    </svg>

    <header class="brand">
      <span class="brand__dot"></span>
      <span class="brand__name">Fenrow Labs</span>
    </header>

    <section class="person">
      <h1 class="person__name"><span class="person__first">Tomas</span> <span class="person__last">Varga</span></h1>
      <p class="person__role">Solution Manager</p>
    </section>

    <ul class="contacts">
      <li class="contact">
        <span class="contact__icon">
          <svg viewBox="0 0 24 24" aria-hidden="true"><path fill="#1a8fd1" d="M3 8c0-2 2-3.5 9-3.5S21 6 21 8v1.5h-4.5V8h-9v1.5H3z M6.5 11h11l2.5 7H4z"/><circle cx="12" cy="14.5" r="2" fill="#fff"/></svg>
        </span>
        <span class="contact__text">024 . 318. 5927<br>024 . 318. 5927</span>
      </li>
      <li class="contact">
        <span class="contact__icon">
          <svg viewBox="0 0 24 24" aria-hidden="true" fill="none" stroke="#1a8fd1" stroke-width="1.8"><circle cx="12" cy="12" r="9"/><ellipse cx="12" cy="12" rx="4" ry="9"/><path d="M3 12h18M4.5 7.5h15M4.5 16.5h15"/></svg>
        </span>
        <span class="contact__text">info@fenrowlabs.cz<br>www.quillbarkgroup.cz</span>
      </li>
      <li class="contact">
        <span class="contact__icon">
          <svg viewBox="0 0 24 24" aria-hidden="true"><path fill="#1a8fd1" d="M12 2a7 7 0 0 0-7 7c0 5 7 13 7 13s7-8 7-13a7 7 0 0 0-7-7z"/><circle cx="12" cy="9" r="2.6" fill="#fff"/></svg>
        </span>
        <span class="contact__text">1418 Harlow Street<br>Kestrel, AK 99615</span>
      </li>
    </ul>
  </main>
</body>
</html>
```